Letterhead and Envelopes design using existing logo. Logo can be found at tqvanholt.com

Use existing logo (attached) and incorporate in letterhead and envelope designs.

Current logo can be viewed at tqvanholt.com the web site reflect various parent and sub companies. Please see attached as well.

Target Market(s)

Other oil and gas operators.

Industry/Entity Type

Oil And Gas

Font styles to use
Sans Serif

Colors

Designer to choose colors to be used in the design.

Requirements
Must have
• Current logo and address
Nice to have
• Modern, contemporary approach yet incorporate existing traditional design.
• After design is selected for Wexford Tiller Holdings I will use similar design for Royalties, Exploration, Energy and Farms with different color schemes.

```html
<!DOCTYPE html>
<html lang="en">
<head>
<meta charset="utf-8">
<title>Wexford Tiller Holdings — Letterhead</title>
<link rel="stylesheet" href="https://fonts.googleapis.com/css2?family=Open+Sans:wght@400;600;700&display=swap">
<style>
  :root {
    --backdrop: #d9d9d9;
    --paper: #f5f5f5;
    --brand-green: #5b8c3e;
    --ink: #3a3a3a;
    --ink-dark: #1e1e1e;
    --on-green: #ffffff;
    --signature-tone: #cfcfcf;
  }
  * { box-sizing: border-box; margin: 0; padding: 0; }
  html, body { width: 1200px; height: 914px; overflow: hidden; background: var(--backdrop); }
  body { font-family: "Open Sans", Arial, sans-serif; color: var(--ink); }

  .letterhead {
    position: absolute; left: 300px; top: 33px;
    width: 600px; height: 848px;
    background: var(--paper);
    box-shadow: 0 6px 18px rgba(0,0,0,.18);
    overflow: hidden;
  }

  .brand-lockup {
    position: absolute; display: flex; align-items: center; gap: 8px;
    font-weight: 700; font-size: 12px; color: var(--ink-dark); white-space: nowrap;
  }
  .brand-lockup .brand-dot {
    width: 22px; height: 22px; border-radius: 50%; background: var(--brand-green); flex: none;
  }
  .brand-lockup--header { left: 40px; top: 92px; }
  .brand-lockup--footer { right: 20px; top: 756px; }

  .header-band {
    position: absolute; left: 248px; right: 0; top: 96px; height: 24px;
    background: var(--brand-green); border-radius: 12px 0 0 12px;
    color: var(--on-green); font-size: 8.5px; line-height: 24px; text-align: right; padding-right: 24px;
  }

  .letter-body { position: absolute; left: 70px; top: 190px; width: 470px; }
  .salutation { font-family: Arial, Helvetica, sans-serif; font-weight: 700; font-size: 14px; color: var(--ink-dark); margin-bottom: 8px; }
  .letter-body p { font-size: 11.5px; line-height: 1.45; margin-bottom: 14px; }

  .signature {
    width: 110px; height: 48px; margin-top: 10px;
    background: var(--signature-tone); border-radius: 4px;
  }

  .footer-band {
    position: absolute; left: 0; width: 392px; top: 760px; height: 24px;
    background: var(--brand-green); border-radius: 0 12px 12px 0;
    color: var(--on-green); font-size: 9px; line-height: 24px; padding-left: 22px; white-space: nowrap;
  }
  .footer-band b { font-weight: 700; }
  .footer-band .sep { margin: 0 6px; }
</style>
</head>
<body>
  <main class="letterhead">
    <div class="brand-lockup brand-lockup--header"><span class="brand-dot"></span>Wexford Tiller Holdings</div>
    <div class="header-band">Wexford Tiller Holdings, LLC. PO Box 318 Linden Ridge, Montana 59407</div>

    <section class="letter-body">
      <h1 class="salutation">Dear Mr. Hale,</h1>
      <p>Lorem Ipsum is simply dummy text of the printing and typesetting industry. Lorem Ipsum has been the industry's standard dummy text ever since the 1500s, when an unknown printer took a galley of type and scrambled it to make a type specimen book. It has survived not only five centuries, but also the leap into electronic typesetting, remaining essentially unchanged.</p>
      <p>The standard chunk of Lorem Ipsum used since the 1500s is reproduced below for those interested. Sections 1.10.32 and 1.10.33 from "de Finibus Bonorum et Malorum" by Cicero are also reproduced in their exact original form, accompanied by English versions from the 1914 translation by H. Rackham</p>
      <p>Lorem Ipsum is simply dummy text of the printing and typesetting industry. Lorem Ipsum has been the industry's standard dummy text ever since the 1500s, when an unknown printer took a galley of type and scrambled it to make a type specimen book. It has survived not only five centuries, but also the leap into electronic typesetting, remaining essentially unchanged. It was popularised in the</p>
      <p>The standard chunk of Lorem Ipsum used since the 1500s is reproduced below for those interested. Sections 1.10.32 and 1.10.33 from "de Finibus Bonorum et Malorum" by Cicero are also reproduced in their exact original form, accompanied by English versions from the 1914 translation by H. Rackham</p>
      <p>The standard chunk of Lorem Ipsum used since the 1500s is reproduced below for those interested. Sections 1.10.32 and 1.10.33 from "de Finibus Bonorum et Malorum" by Cicero are also reproduced in their exact original form.</p>
      <div class="signature" role="img" aria-label="Handwritten signature of the sender"></div>
    </section>

    <div class="footer-band">
      <b>P. :</b> (406) 555.0142<span class="sep">|</span><b>E. :</b> reception@tqvanholt.com<span class="sep">|</span><b>W. :</b> www.tqvanholt.com
    </div>
    <div class="brand-lockup brand-lockup--footer"><span class="brand-dot"></span>Wexford Tiller Holdings</div>
  </main>
</body>
</html>
```